New Pump Website Design Needed

We need a homepage concept for a pump website rebuild.

The navigation at the top must be:
Home - About Us - Pump Stations - Pumps - Electrical - Drainage - Environmental - Accessories - Contact Us

The homepage should have the the following structure:
Logo
Navigation
Rotating Banner
Content + Picture of PDF Flipbook to download/ view
Featured Products (in one row - approx 4)
Footer

The footer must include:
Left side - navigation small.
"Copyright RiverWell 2014. All Rights reserved"

Right side: "Website by Pagecraft Studio"

Content and imagery, and Logo can be taken from their existing website: tidelinehydro.co.nz

We have attached a copy of their New PDF - the new website design must reflect this (Use block colours/ different colours for the navigation items/ incorporate the footer image).

Industry/Entity Type

Electrical

Font styles to use
Sans Serif

Requirements
Must have
• Features from their brochure brought in (colour scheme and footer feature)
Should not have
• Any Social Media Icons

```html
<!DOCTYPE html>
<html lang="en">
<head>
<meta charset="utf-8">
<title>RiverWell Pump Systems</title>
<link rel="stylesheet" href="https://fonts.googleapis.com/css2?family=Oswald:wght@400;500;700&family=Open+Sans:wght@400;600;700&display=swap">
<style>
:root{
  --red:#c8161d;
  --red-dark:#a30f15;
  --ink:#3a3a3a;
  --muted:#7a7a7a;
  --line:#d6d6d6;
  --band:#ececec;
  --nav:#e4e4e4;
  --dark:#3b3b3b;
  --darker:#2a2a2a;
  --white:#ffffff;
  --blue:#1f4f8f;
}
*{box-sizing:border-box;margin:0;padding:0}
html,body{width:1200px;height:2316px;overflow:hidden}
body{background:var(--white);font-family:"Open Sans",Arial,sans-serif;color:var(--ink);position:relative}

.site-header{height:160px;position:relative}
.brand{position:absolute;left:32px;top:24px;display:flex;align-items:center;gap:14px}
.brand-mark{width:44px;height:44px;background:var(--blue)}
.brand-name{font-family:"Oswald",sans-serif;font-weight:700;font-size:52px;color:var(--blue);line-height:1;letter-spacing:1px}
.brand-tag{position:absolute;left:90px;top:90px;font-family:"Oswald",sans-serif;font-size:22px;color:var(--red);letter-spacing:1px}
.promo{position:absolute;left:648px;top:20px;width:520px;height:112px;background:var(--red);color:var(--white);text-align:center;font-family:"Oswald",sans-serif;border:3px solid var(--red-dark)}
.promo-small{font-size:26px;letter-spacing:1px;margin-top:6px;line-height:30px}
.promo-big{font-size:64px;font-weight:700;line-height:66px;letter-spacing:2px}

.main-nav{position:absolute;top:160px;left:0;width:1200px;height:40px;background:var(--nav);border-top:1px solid var(--line);border-bottom:1px solid var(--line)}
.main-nav ul{list-style:none;display:flex;padding-left:120px}
.main-nav li{font-size:15px;line-height:38px;padding:0 20px;color:#555;border-right:1px solid var(--line)}
.main-nav li.active{color:var(--red);font-weight:600}

.banner{position:absolute;top:200px;left:100px;width:1000px;height:400px;background:linear-gradient(135deg,#6e7c8c 0%,#9aa7b3 35%,#3a6fb0 60%,#c9ced3 100%)}

.section-title{position:absolute;left:100px;width:1000px;text-align:center;font-family:"Oswald",sans-serif;font-weight:500;font-size:36px;line-height:44px;color:var(--ink);letter-spacing:1px}
.section-title::before,.section-title::after{content:"";position:absolute;top:50%;width:230px;height:1px;background:var(--line)}
.section-title::before{left:0}.section-title::after{right:0}
.t-welcome{top:620px}
.t-info{top:1186px}

.feature-band{position:absolute;top:676px;left:0;width:1200px;height:484px;background:linear-gradient(#f6f6f6,var(--band))}
.feature{position:absolute;top:86px;width:300px;height:300px;border-radius:50%;border:8px solid var(--white);box-shadow:0 2px 8px rgba(0,0,0,.25)}
.f1{left:142px;background:radial-gradient(circle,#8a9099,#4a5058)}
.f2{left:450px;background:radial-gradient(circle,#9aa0a8,#54606c)}
.f3{left:758px;background:radial-gradient(circle,#b0b4ba,#3a4048)}

.info{position:absolute;top:1270px;width:460px}
.info-left{left:120px}
.info-right{left:690px}
.info h3{font-family:"Oswald",sans-serif;font-weight:500;font-size:30px;color:var(--red);margin-bottom:10px;letter-spacing:.5px}
.info p{font-size:15px;line-height:22px;color:var(--muted);margin-bottom:14px}
.info section{margin-bottom:22px}

.lower{position:absolute;top:1848px;left:0;width:1200px;height:376px;background:var(--dark);color:#ddd}
.lower h2{font-family:"Oswald",sans-serif;font-weight:500;font-size:32px;line-height:40px;color:var(--white);letter-spacing:1px;white-space:nowrap}
.lower-welcome{position:absolute;left:100px;top:24px}
.lower-photo{position:absolute;left:100px;top:84px;width:340px;height:250px;background:linear-gradient(160deg,#b9c6d2,#e6e6e6 50%,#7d8790)}
.lower-text{position:absolute;left:464px;top:84px;width:290px}
.lower-text h4{font-family:"Oswald",sans-serif;font-weight:500;font-size:22px;color:var(--white);margin-bottom:10px}
.lower-text p{font-size:14px;line-height:21px;color:#bdbdbd}
.office{position:absolute;left:772px;top:24px;width:400px;height:330px;border-left:1px solid #555;padding-left:22px}
.office h4{font-size:16px;color:var(--white);margin:18px 0 8px;font-weight:600}
.office p{font-size:14px;line-height:21px;color:#bdbdbd}
.office .free{font-size:18px;color:var(--white);margin:12px 0 6px;font-weight:600}
.office dl{display:grid;grid-template-columns:60px 1fr;font-size:14px;line-height:22px;color:#bdbdbd}

.site-footer{position:absolute;top:2224px;left:0;width:1200px;height:92px;background:var(--red);color:var(--white);text-align:center;font-size:14px}
.site-footer nav{padding-top:14px}
.site-footer .legal{display:flex;justify-content:space-between;width:1000px;margin:6px auto 0}
.site-footer .strip{position:absolute;bottom:0;left:0;width:1200px;height:28px;background:var(--darker)}
</style>
</head>
<body>
<header class="site-header">
  <div class="brand">
    <span class="brand-mark"></span>
    <span class="brand-name">RiverWell</span>
  </div>
  <div class="brand-tag">Dependable Water Movement</div>
  <div class="promo">
    <div class="promo-small">IF YOU'RE BELOW THE SEWER LINE</div>
    <div class="promo-big">GET ONLINE</div>
  </div>
</header>

<nav class="main-nav">
  <ul>
    <li class="active">Home</li><li>About Us</li><li>Pump Stations</li><li>Pumps</li><li>Electrical</li><li>Drainage</li><li>Environmental</li><li>Accessories</li><li>Contact Us</li>
  </ul>
</nav>

<div class="banner" role="img" aria-label="Pump station equipment with blue pumps and motors"></div>

<h2 class="section-title t-welcome">WELCOME TO TIDELINE HYDRO</h2>
<div class="feature-band">
  <div class="feature f1" role="img" aria-label="Grey submersible pump"></div>
  <div class="feature f2" role="img" aria-label="Pump with electric motor"></div>
  <div class="feature f3" role="img" aria-label="Vacuum pump unit"></div>
</div>

<h2 class="section-title t-info">GENERAL/PRODUCT INFORMATION</h2>
<div class="info info-left">
  <section><h3>PRODUCT RANGE</h3>
    <p>The RiverWell Products shown in this catalogue are a selection of both local and imported quality products from reputable well established companies and manufacturers.</p>
    <p>We would like to emphasise that our product range is not limited to what's in the catalogue, therefore if you can't find what you're looking for please give us a call.</p></section>
  <section><h3>FREIGHT</h3>
    <p>Orders over $300 plus GST are freight free. Orders under this amount will incur freight charges. NB: This excludes the Slimline City Tanks and Above Ground Water Tanks.</p></section>
  <section><h3>AVAILABILITY</h3>
    <p>Please give us a call to check on RiverWell Product availability. This can vary from day to day depending on demand or other factors that are beyond our control.</p></section>
</div>
<div class="info info-right">
  <section><h3>TECHNICAL SUPPORT</h3>
    <p>The RiverWell Pump Systems Sales Team is available to discuss any technical queries to assist in selection of products, or submit a quotation to meet a specific requirement. This includes working with individual clients including Plumbers, Developers, Architects, Designers and Developers to establish their exact requirements and then liaising with their chosen Plumbing Merchant.</p></section>
  <section><h3>WARRANTY</h3>
    <p>All RiverWell Product Warranties are shown on the respective product sheets. The warranty period is from date of invoice against faulty parts and workmanship.</p></section>
  <section><h3>SPECIFICATIONS</h3>
    <p>RiverWell Product Specification may change at any time without notice, due to design and product enhancement.</p></section>
</div>

<section class="lower">
  <h2 class="lower-welcome">WELCOME</h2>
  <div class="lower-photo" role="img" aria-label="Installed pump station tanks on site"></div>
  <div class="lower-text">
    <h4>LOREM IPSUM DOLOR SIT</h4>
    <p>Lorem ipsum dolor sit amet, consectetur adipiscing elit, sed diam nonummy nibh euismod tincidunt ut laoreet dolore magna aliquam erat volutpat. Ut wisi enim ad minim veniam, quis nostrud exerci tation ullamcorper suscipit lobortis nisl ut aliquip ex ea commodo consequat.</p>
  </div>
  <div class="office">
    <h2>OFFICE LOCATIONS/CONTACT</h2>
    <h4>WELLINGTON OFFICE</h4>
    <p>14 Tasman St<br>Petone<br>Wellington</p>
    <p class="free">FREEPHONE 0800 555 214</p>
    <dl><dt>Phone</dt><dd>+64 4 555 0300</dd><dt>Fax</dt><dd>+64 4 555 0310</dd><dt>Email</dt><dd>sales@riverwell.co.nz</dd></dl>
  </div>
</section>

<footer class="site-footer">
  <nav>Home | About Us | Pump Stations | Pumps | Electrical | Drainage | Environmental | Accessories | Contact Us</nav>
  <div class="legal"><span>Copyright RiverWell 2014. All Rights reserved</span><span>Website by Pagecraft Studio</span></div>
  <div class="strip"></div>
</footer>
</body>
</html>
```